New Business Card Design

we need a new business card as we have just moved location and need a fresh new look. we are a Land Surveying Company . the card needs to be 2 sided and needs to have what we do on the back as our previous card ( attached ).
i was thinking of maybe a ruler down the bottom of the card or something to make it stand out. size can be 90 x 55 or 90 x 45 .
maybe a shadow of the logo or something in the corner.
on the attached card where it says other offices , it should be Melbourne instead of bendigo

postal address should be there as PO box 812 , Thornbury Flats 3821
Updates

Reason: some designs didn't follow brief by having services provided on the back of the card, just giving a bit of time toi change and to review.

Industry/Entity Type

Business

Requirements
Must have
• All cards need to have services provided on the back please , as stated , a lot of designs have just had the logo on the back

```html
<!DOCTYPE html>
<html lang="en">
<head>
<meta charset="utf-8">
<title>Marlow Quinn Land Surveyors – Business Card</title>
<link href="https://fonts.googleapis.com/css2?family=Roboto:wght@400;500;700&display=swap" rel="stylesheet">
<style>
  :root {
    --bg: #c9c9cb;
    --card: #ffffff;
    --ink: #2b2b2b;
    --grey-text: #6f6f72;
    --blue: #1f7fcf;
    --navy: #0f2a47;
    --mid-blue: #1d6fae;
    --steel: #8fa0aa;
    --steel-light: #c3ccd1;
  }
  * { box-sizing: border-box; margin: 0; padding: 0; }
  html, body { width: 1200px; height: 861px; overflow: hidden; }
  body {
    background: var(--bg);
    font-family: "Roboto", Arial, sans-serif;
    color: var(--ink);
    position: relative;
  }
  .card {
    position: absolute;
    top: 272px;
    width: 520px;
    height: 318px;
    background: var(--card);
    overflow: hidden;
    box-shadow: 0 6px 18px rgba(0,0,0,0.18);
  }
  .card--back { left: 50px; }
  .card--front { left: 630px; }
  .bands { position: absolute; left: 0; top: 0; width: 520px; height: 318px; }

  .brand { position: absolute; display: flex; align-items: center; gap: 10px; }
  .brand__dot {
    width: 44px; height: 44px; border-radius: 50%;
    background: var(--blue);
  }
  .brand__name {
    font-weight: 700; color: var(--ink);
    font-size: 25px; line-height: 1; letter-spacing: 0.5px;
    text-transform: uppercase;
  }
  .brand__name small {
    display: block; font-size: 13px; letter-spacing: 4.2px; margin-top: 3px;
  }

  /* back */
  .card--back .brand { left: 130px; top: 28px; }
  .services {
    position: absolute; left: 30px; top: 94px; width: 470px;
    list-style: none; font-size: 12.5px; line-height: 1.45; color: var(--ink);
  }
  .services li::before { content: "• "; color: var(--blue); font-weight: 700; }
  .memberships {
    position: absolute; left: 0; width: 100%; top: 168px;
    text-align: center; font-size: 10px; line-height: 1.5; color: var(--ink);
  }
  .memberships__offices { margin-top: 5px; }

  /* front */
  .card--front .brand { left: 190px; top: 110px; }
  .person { position: absolute; left: 30px; top: 196px; width: 195px; text-align: right; }
  .person__name { color: var(--blue); font-weight: 700; font-size: 19px; }
  .person__quals { color: var(--grey-text); font-size: 12px; line-height: 1.35; margin-top: 3px; }
  .person__role { font-weight: 700; font-size: 12px; line-height: 1.35; }
  .divider { position: absolute; left: 243px; top: 172px; width: 1px; height: 120px; background: #888; }
  .contact { position: absolute; left: 258px; top: 170px; font-size: 10.5px; line-height: 1.45; }
  .contact dl { display: grid; grid-template-columns: 14px auto; margin-top: 6px; }
  .contact dt { color: var(--blue); font-weight: 700; }
</style>
</head>
<body>

<section class="card card--back" aria-label="Card back – services">
  <svg class="bands" viewBox="0 0 520 318" aria-hidden="true">
    <polygon points="0,318 0,278 520,200 520,318" fill="var(--steel-light)"/>
    <polygon points="0,318 0,292 520,218 520,318" fill="var(--steel)"/>
    <polygon points="0,318 0,304 520,236 520,318" fill="var(--navy)"/>
    <polygon points="90,318 520,250 520,270 180,318" fill="var(--mid-blue)"/>
  </svg>
  <div class="brand">
    <span class="brand__dot"></span>
    <span class="brand__name">Marlow Quinn<small>Land Surveyors</small></span>
  </div>
  <ul class="services">
    <li>Subdivisions (Land and Building) • Check Title Boundary Surveys</li>
    <li>Features and Level Surveys • Neighbourhood and Site Description</li>
    <li>Plan for Development Permits • Town Planning/ Estate Design</li>
    <li>Civil Engineering Surveys (Roads, Structural, and Earthworks</li>
  </ul>
  <div class="memberships">
    <p>Member of Regional Surveyors Association<br>
    Member of Land Development Council of Australia</p>
    <p class="memberships__offices">Other Offices: Calder Vale</p>
  </div>
</section>

<section class="card card--front" aria-label="Card front – contact">
  <svg class="bands" viewBox="0 0 520 318" aria-hidden="true">
    <polygon points="0,0 520,0 520,55 0,185" fill="var(--steel-light)"/>
    <polygon points="0,0 520,0 520,38 0,160" fill="var(--steel)"/>
    <polygon points="0,0 520,0 520,22 0,140" fill="var(--navy)"/>
    <polygon points="0,70 520,2 520,14 0,105" fill="var(--mid-blue)"/>
  </svg>
  <div class="brand">
    <span class="brand__dot"></span>
    <span class="brand__name">Marlow Quinn<small>Land Surveyors</small></span>
  </div>
  <div class="person">
    <p class="person__name">Daniel Quinn</p>
    <p class="person__quals">B.App.Sci.(Surv) MIS(Aust)<br>Grad.Dip.(Surv Prac)</p>
    <p class="person__role">Licensed Surveyor<br>Director</p>
  </div>
  <span class="divider"></span>
  <div class="contact">
    <p>Cnr Ashby Lane and Corella Street,<br>Ridgewood VIC 3460</p>
    <p>PO box 812 , Thornbury Flats 3821</p>
    <dl>
      <dt>T</dt><dd>03 5550 1274</dd>
      <dt>F</dt><dd>03 5550 1288</dd>
      <dt>M</dt><dd>0400 555 019</dd>
      <dt>E</dt><dd>daniel@marlowquinn.com.au</dd>
      <dt>W</dt><dd>www.marlowquinn.com.au</dd>
    </dl>
  </div>
</section>

</body>
</html>
```